ART/CASTING RESIN LABEL

Clear label for bottle of art/casting epoxy. It needs to be fun,artsy,colorful.
My brand is QUILLO RESIN should read ART/CASTING RESIN.
Attached are a couple of my competitors labels for inspiration
Updates

The bottles will be clear . 12 ounce and 6 ounce. I need the purchaser to see that the resin is crystal clear like water so their project turns out crystal clear..

Target Market(s)

DIY -ARTIST-

Font styles to use
Decorative

Requirements
Must have
• Color and fun

```html
<!DOCTYPE html>
<html lang="en">
<head>
<meta charset="utf-8">
<title>Quillo Resin – Art / Casting Resin Label</title>
<link rel="stylesheet" href="https://fonts.googleapis.com/css2?family=Montserrat:wght@500;800&display=swap">
<style>
  :root {
    --page-bg: #ffffff;
    --band-red: #e61f30;
    --band-yellow: #f5e012;
    --ink: #111111;
    --blob-white: #ecefee;
    --art-pink-light: #f6dbe6;
    --art-pink: #f4a6c6;
    --art-magenta: #ec1a68;
    --art-yellow: #f4e11b;
    --art-purple: #9a7dbb;
    --art-green: #6dbd4a;
  }
  html, body {
    margin: 0;
    width: 1200px;
    height: 1200px;
    overflow: hidden;
    background: var(--page-bg);
  }
  .canvas {
    width: 1200px;
    height: 1200px;
    display: flex;
    align-items: center;
    justify-content: center;
  }
  .label {
    width: 484px;
    height: 1080px;
    display: flex;
    flex-direction: column;
    box-shadow: 0 0 0 1px rgba(0,0,0,0.04);
  }
  .label__top-band {
    height: 74px;
    background: var(--band-red);
    display: flex;
    align-items: center;
    justify-content: center;
    font-family: "Montserrat", sans-serif;
    font-weight: 500;
    font-size: 24px;
    letter-spacing: 0.16em;
    color: var(--ink);
  }
  .label__artwork {
    position: relative;
    flex: 1;
    background:
      linear-gradient(180deg,
        var(--art-pink) 0%,
        var(--art-pink-light) 24%,
        var(--art-yellow) 40%,
        var(--art-magenta) 52%,
        var(--art-yellow) 66%,
        var(--art-purple) 84%,
        var(--art-green) 100%);
  }
  .label__brand-blob {
    position: absolute;
    left: 116px;
    top: 60px;
    width: 286px;
    height: 140px;
  }
  .label__brand-name {
    position: absolute;
    left: 116px;
    top: 60px;
    width: 286px;
    height: 140px;
    display: flex;
    align-items: center;
    justify-content: center;
    font-family: "Montserrat", sans-serif;
    font-weight: 800;
    font-size: 34px;
    color: var(--ink);
    margin: 0;
  }
  .label__bottom-band {
    height: 55px;
    background: var(--band-yellow);
    display: flex;
    align-items: center;
    justify-content: center;
    font-family: "Montserrat", sans-serif;
    font-weight: 500;
    font-size: 24px;
    letter-spacing: 0.14em;
    color: var(--ink);
  }
</style>
</head>
<body>
  <main class="canvas">
    <article class="label">
      <header class="label__top-band">ART / CASTING RESIN</header>
      <section class="label__artwork" role="img" aria-label="Colourful jungle illustration with pink sky, tropical leaves and flowers, and a small bird perched on the right">
        <svg class="label__brand-blob" viewBox="0 0 286 140" aria-hidden="true">
          <path d="M30 40 C60 0 200 -6 250 20 C292 44 292 104 244 124 C190 146 80 144 36 122 C-4 102 -4 66 30 40 Z" fill="var(--blob-white)"/>
        </svg>
        <h1 class="label__brand-name">QUILLO RESIN</h1>
      </section>
      <footer class="label__bottom-band">12 OUNCE</footer>
    </article>
  </main>
</body>
</html>
```